Poster for Display Sign - Pet Related

Looking for a poster for my brochure display rack. The display rack will be taken to trade shows and the sign should catch attention of our audience as they pass by.
The poster frame size is 24" x 36". The view able area is 23" x 35".
We are a pet product delivery service for our local community. The sign should communicate trust and be personable and inviting.
The final design should also be sent in a format that can be printed to any size.
You can visit our website at: www.BrightTailRoutes.com to get a feel for our company.
Target Market(s)
Higher than average households looking to make their lives easier by having their pet products delivered to their door.
Industry/Entity Type
Delivery Service
Requirements
Must have
- Logo, image of dogs/cats/person with their pet, web address: www.BrightTailRoutes.com, phone number: 555-318-2076.
Can play around with the text of either: Sit. Stay. Let us Fetch! Or, making your life easier, theirs healthier and happier.
Nice to have
- Use of our colors: orange, blue and green.
If space allows, can contain the text: Owning a pet is an amazing experience, but there is no denying that one of the least enjoyable aspects of pet ownership is driving to the store to buy pet food. Getting premium pet products delivered right to your door has never been easier. At Bright Tail, we strive to make one of the most inconvenient parts of pet ownership as hassle and worry free as possible.
Should not have
- Delivery trucks/cars, lots of random paw prints.

```html
<!DOCTYPE html>
<html lang="en">
<head>
<meta charset="utf-8">
<title>Bright Tail – Premium Pet Products Delivered</title>
<link href="https://fonts.googleapis.com/css2?family=Pacifico&family=Open+Sans:wght@400;600&display=swap" rel="stylesheet">
<style>
  :root {
    --orange: #f47b20;
    --orange-soft: #f39223;
    --blue: #36a9e1;
    --green: #8dc63f;
    --ink: #4d4d4d;
    --ink-dark: #222;
    --paper: #ffffff;
    --grass-light: #8cc25a;
    --grass-dark: #5a9434;
  }
  html, body { margin: 0; padding: 0; overflow: hidden; background: var(--paper); }
  .poster {
    position: relative;
    width: 789px;
    height: 1200px;
    overflow: hidden;
    background: var(--paper);
    font-family: "Open Sans", Arial, sans-serif;
  }
  .accent-bar { position: absolute; z-index: 1; }
  .accent-bar--blue { left: 0; top: 93px; width: 181px; height: 23px; background: var(--blue); }
  .accent-bar--orange { left: 181px; top: 60px; width: 608px; height: 83px; background: var(--orange); }
  .accent-bar--footer { left: 0; top: 1168px; width: 789px; height: 32px; background: var(--orange); }

  .hero-photo {
    position: absolute;
    left: 0; top: 116px;
    width: 789px; height: 604px;
    z-index: 0;
    background: linear-gradient(180deg, var(--grass-light) 0%, var(--grass-dark) 100%);
  }

  .headline {
    position: absolute;
    margin: 0;
    color: var(--paper);
    font-family: "Pacifico", cursive;
    font-weight: 400;
    font-size: 51px;
    line-height: 1;
    display: flex;
    align-items: center;
    box-sizing: border-box;
    white-space: nowrap;
    z-index: 2;
  }
  .headline--top { left: 0; top: 664px; width: 629px; height: 76px; padding-left: 64px; background: var(--orange-soft); }
  .headline--bottom { left: 143px; top: 741px; width: 630px; height: 77px; padding-left: 16px; background: var(--blue); }

  .intro {
    position: absolute;
    left: 44px; top: 893px;
    width: 294px;
    margin: 0;
    font-size: 11.8px;
    line-height: 16.3px;
    letter-spacing: 0.5px;
    color: var(--ink);
    text-align: justify;
    hyphens: auto;
    -webkit-hyphens: auto;
  }
  .contact {
    position: absolute;
    left: 44px; top: 1045px;
    width: 294px;
    text-align: center;
    font-size: 16px;
    line-height: 21px;
    color: var(--ink-dark);
    letter-spacing: 0.3px;
  }
  .contact a { color: inherit; text-decoration: none; display: block; }

  .motto { position: absolute; left: 396px; top: 888px; width: 340px; height: 130px; }
  .motto svg { display: block; }
  .motto-text {
    position: absolute; left: 0; top: 0; width: 100%; height: 100%;
    display: flex; align-items: center; justify-content: center;
    margin: 0;
    color: var(--paper);
    font-family: "Pacifico", cursive;
    font-size: 28px;
    white-space: nowrap;
  }

  .brand {
    position: absolute;
    left: 590px; top: 1088px;
    width: 180px;
    text-align: right;
    color: #777;
  }
  .brand-name { display: block; font-size: 27px; line-height: 30px; font-weight: 400; }
  .brand-tagline { display: block; font-size: 9.6px; letter-spacing: 0.2px; font-style: italic; color: #8a8a8a; margin-top: 10px; white-space: nowrap; }
</style>
</head>
<body>
<main class="poster">
  <div class="hero-photo" role="img" aria-label="Smiling woman sitting on the grass hugging a golden retriever and holding an orange and white cat"></div>
  <div class="accent-bar accent-bar--blue"></div>
  <div class="accent-bar accent-bar--orange"></div>

  <h1 class="headline headline--top">Making your life easier</h1>
  <h2 class="headline headline--bottom">theirs healthier and happier</h2>

  <p class="intro">Owning a pet is an amazing experience, but there is no denying that one of the least enjoyable aspects of pet ownership is driving to the store to buy pet food. Getting premium pet products delivered right to your door has never been easier. At Bright Tail, we strive to make one of the most inconvenient parts of pet ownership as hassle and worry free as possible.</p>

  <div class="contact">
    <a href="http://www.BrightTailRoutes.com">www.BrightTailRoutes.com</a>
    <a href="tel:5553182076">555-318-2076</a>
  </div>

  <div class="motto">
    <svg width="340" height="130" viewBox="0 0 340 130" aria-hidden="true">
      <circle cx="64" cy="65" r="63" fill="#f39223"/>
      <circle cx="176" cy="65" r="62" fill="#8dc63f" opacity="0.92"/>
      <circle cx="274" cy="65" r="63" fill="#36a9e1" opacity="0.95"/>
      <path d="M120 35 A63 63 0 0 1 120 95 A62 62 0 0 1 120 35 Z" fill="#9a7a25" opacity="0.5"/>
    </svg>
    <p class="motto-text">Sit. Stay. Let us Fetch!</p>
  </div>

  <div class="brand">
    <span class="brand-name">Bright Tail</span>
    <span class="brand-tagline">PREMIUM PET PRODUCTS DELIVERED</span>
  </div>

  <div class="accent-bar accent-bar--footer"></div>
</main>
</body>
</html>
```